Custom Monogramming and Retail gifts

We need a Business Card for a monogramming business that offers many retail gift options. We are a home based business that uses social media (Chatterbox,clipboardia and our website) to sell our products. Our target market is college age, high school, baby gifts.
We want a preppy fun look. Monogramming is very popular in the South

Industry/Entity Type

College

Contact Information for Business Card

Threadwell Keepsakes
Custom Monogramming and Gifts
7152 Brackenway Lane
Gainesville, GA 30999
Della Marsh, Owner
555-314-2790
threadwellkeepsakes.example
threadwellkeepsakes@mailbox.example

```html
<!DOCTYPE html>
<html lang="en">
<head>
<meta charset="utf-8">
<title>Threadwell Keepsakes – Business Card</title>
<link rel="stylesheet" href="https://fonts.googleapis.com/css2?family=PT+Sans+Narrow:wght@400;700&display=swap">
<style>
  :root {
    --backdrop: #e9e9ea;
    --card: #fbfbfb;
    --pink: #d9357a;
    --ink: #1c1c1c;
    --white: #ffffff;
  }
  * { box-sizing: border-box; margin: 0; padding: 0; }
  html, body {
    width: 1200px; height: 1000px; overflow: hidden;
    background: var(--backdrop);
    font-family: "PT Sans Narrow", "Arial Narrow", sans-serif;
  }
  .card {
    position: absolute; left: 100px; top: 214px;
    width: 1000px; height: 572px;
    background: var(--card);
    box-shadow: 0 6px 18px rgba(0,0,0,0.12);
    overflow: hidden;
  }
  .name-panel {
    position: absolute; left: 560px; top: 0;
    width: 330px; height: 165px;
    background: var(--pink);
    color: var(--white);
    text-align: right;
    padding: 48px 36px 0 0;
  }
  .name-panel .person { font-size: 36px; font-weight: 700; line-height: 1; }
  .name-panel .role { font-size: 21px; margin-top: 6px; }
  .edge-tab { position: absolute; right: 0; width: 80px; height: 34px; }
  .edge-tab.first { top: 196px; }
  .edge-tab.second { top: 300px; }
  .contact {
    position: absolute; left: 590px; color: var(--ink);
    font-size: 26px; line-height: 32px;
  }
  .contact.address { top: 198px; }
  .contact.online { top: 330px; }
  .row { display: flex; align-items: center; gap: 10px; white-space: nowrap; }
  .row.indent { padding-left: 26px; }
  .icon { width: 18px; height: 18px; flex: none; }
  .brand {
    position: absolute; left: 70px; top: 360px;
    display: flex; align-items: center; gap: 18px;
  }
  .brand-dot { width: 26px; height: 26px; border-radius: 50%; background: var(--pink); }
  .brand-name {
    font-size: 56px; font-weight: 700; color: var(--pink); line-height: 1.05;
  }
</style>
</head>
<body>
  <div class="card">
    <div class="name-panel">
      <div class="person">Della Marsh</div>
      <div class="role">Owner</div>
    </div>

    <svg class="edge-tab first" viewBox="0 0 80 34" aria-hidden="true">
      <path d="M80 0H8l-4 4 4 4-4 4 4 4-4 4 4 4-4 4 4 4-4 2h76z" fill="var(--pink)"/>
    </svg>
    <svg class="edge-tab second" viewBox="0 0 80 34" aria-hidden="true">
      <path d="M80 0H8l-4 4 4 4-4 4 4 4-4 4 4 4-4 4 4 4-4 2h76z" fill="var(--pink)"/>
    </svg>

    <div class="contact address">
      <div class="row">
        <svg class="icon" viewBox="0 0 18 18" aria-hidden="true"><path d="M9 1a6 6 0 0 0-6 6c0 4.5 6 10 6 10s6-5.5 6-10a6 6 0 0 0-6-6zm0 8.5A2.5 2.5 0 1 1 9 4.5a2.5 2.5 0 0 1 0 5z" fill="var(--pink)"/></svg>
        <span>7152 Brackenway Lane</span>
      </div>
      <div class="row indent"><span>Gainesville, GA 30999</span></div>
      <div class="row indent">
        <svg class="icon" viewBox="0 0 18 18" aria-hidden="true"><rect x="4" y="1" width="10" height="16" rx="2" fill="none" stroke="var(--pink)" stroke-width="2"/><circle cx="9" cy="14" r="1.2" fill="var(--pink)"/></svg>
        <span>555-314-2790</span>
      </div>
    </div>

    <div class="contact online">
      <div class="row">
        <svg class="icon" viewBox="0 0 18 18" aria-hidden="true"><rect x="1" y="4" width="16" height="11" fill="var(--pink)"/><path d="M1 4l8 6 8-6" fill="none" stroke="var(--white)" stroke-width="1.5"/></svg>
        <span>threadwellkeepsakes@mailbox.example</span>
      </div>
      <div class="row">
        <svg class="icon" viewBox="0 0 18 18" aria-hidden="true"><rect x="1" y="2" width="16" height="14" fill="var(--pink)"/><rect x="1" y="2" width="16" height="3" fill="#a8225b"/></svg>
        <span>threadwellkeepsakes.example</span>
      </div>
    </div>

    <div class="brand">
      <div class="brand-dot"></div>
      <div class="brand-name">Threadwell<br>Keepsakes</div>
    </div>
  </div>
</body>
</html>
```